Meridale Capital Partners - Real estate loans - need a business card with a logo

I need a logo and a business card that looks elegant - that looks as if it is a big stablish corporation - We do real estate loans, my goal is to brand myself with colors black background - gold or silver letters - some combination - Name of the company different color than the rest of the card -

```html
<!DOCTYPE html>
<html lang="en">
<head>
<meta charset="utf-8">
<title>Meridale Capital Partners – Business Card</title>
<link href="https://fonts.googleapis.com/css2?family=Cinzel:wght@400;600&display=swap" rel="stylesheet">
<style>
  :root {
    --paper: #e4e3e0;
    --card: #050505;
    --gold: #d4ad3c;
    --gold-soft: #b8923a;
    --silver: #e6e6e6;
  }
  * { margin: 0; padding: 0; box-sizing: border-box; }
  html, body { width: 1200px; height: 900px; overflow: hidden; }
  body {
    background: var(--paper);
    font-family: "Cinzel", serif;
    display: flex;
    flex-direction: column;
    align-items: center;
    justify-content: center;
    gap: 36px;
  }
  .card {
    position: relative;
    width: 700px;
    height: 400px;
    background: var(--card);
    border-radius: 6px;
    overflow: hidden;
    box-shadow: 0 10px 24px rgba(0,0,0,.18);
  }
  .card__lines { position: absolute; inset: 0; }
  .brand {
    position: absolute;
    display: flex;
    flex-direction: column;
    align-items: center;
    text-align: center;
    color: var(--gold);
    font-family: "Cinzel", serif;
    font-weight: 600;
  }
  .brand__circle {
    border: 4px solid var(--gold);
    border-radius: 50%;
  }
  .card--back .brand { left: 0; right: 0; top: 78px; }
  .card--back .brand__circle { width: 150px; height: 150px; margin-bottom: 22px; }
  .card--back .brand__name { font-size: 34px; line-height: 1.1; letter-spacing: 1px; }
  .card--front .brand { left: 40px; width: 240px; top: 112px; }
  .card--front .brand__circle { width: 104px; height: 104px; margin-bottom: 16px; }
  .card--front .brand__name { font-size: 22px; line-height: 1.15; }
  .divider {
    position: absolute;
    left: 300px; top: 78px;
    width: 2px; height: 250px;
    background: var(--gold);
  }
  .contact {
    position: absolute;
    left: 330px; top: 120px;
    list-style: none;
    display: flex;
    flex-direction: column;
    gap: 22px;
  }
  .contact__item {
    display: flex;
    align-items: center;
    gap: 14px;
    color: var(--silver);
    font-size: 20px;
    letter-spacing: 2px;
  }
  .contact__icon { width: 22px; height: 22px; flex: none; }
</style>
</head>
<body>

<section class="card card--back" aria-label="Card back">
  <svg class="card__lines" viewBox="0 0 700 400" aria-hidden="true">
    <line x1="430" y1="30" x2="700" y2="8" stroke="var(--gold)" stroke-width="2.5"/>
    <line x1="560" y1="0" x2="700" y2="50" stroke="var(--gold-soft)" stroke-width="1.5"/>
  </svg>
  <div class="brand">
    <div class="brand__circle"></div>
    <div class="brand__name">Meridale<br>Capital Partners</div>
  </div>
</section>

<section class="card card--front" aria-label="Card front">
  <svg class="card__lines" viewBox="0 0 700 400" aria-hidden="true">
    <line x1="440" y1="0" x2="700" y2="44" stroke="var(--gold)" stroke-width="2.5"/>
    <line x1="600" y1="0" x2="700" y2="16" stroke="var(--gold-soft)" stroke-width="1.5"/>
    <line x1="0" y1="330" x2="260" y2="400" stroke="var(--gold)" stroke-width="2.5"/>
    <line x1="0" y1="378" x2="110" y2="400" stroke="var(--gold-soft)" stroke-width="1.5"/>
  </svg>

  <div class="brand">
    <div class="brand__circle"></div>
    <div class="brand__name">Meridale<br>Capital Partners</div>
  </div>

  <div class="divider"></div>

  <ul class="contact">
    <li class="contact__item">
      <svg class="contact__icon" viewBox="0 0 22 22" aria-hidden="true">
        <circle cx="11" cy="11" r="11" fill="var(--gold)"/>
        <path d="M6 11 L11 6.5 L16 11 M7.5 10 V15.5 H14.5 V10" fill="none" stroke="#111" stroke-width="1.3"/>
      </svg>
      <span>Your Adress Goes Here</span>
    </li>
    <li class="contact__item">
      <svg class="contact__icon" viewBox="0 0 22 22" aria-hidden="true">
        <circle cx="11" cy="11" r="11" fill="var(--gold)"/>
        <rect x="6" y="7.5" width="10" height="7" fill="none" stroke="#111" stroke-width="1.3"/>
        <path d="M6 7.5 L11 11.5 L16 7.5" fill="none" stroke="#111" stroke-width="1.3"/>
      </svg>
      <span>yourweb@email.com</span>
    </li>
    <li class="contact__item">
      <svg class="contact__icon" viewBox="0 0 22 22" aria-hidden="true">
        <circle cx="11" cy="11" r="11" fill="var(--gold-soft)"/>
        <path d="M7.5 6.5 C7 9.5 11 15 15 15.2 L15.5 13.2 L13.3 12.2 L12.4 13.2 C11 12.5 9.7 11.2 9 9.8 L10 8.9 L9 6.7 Z" fill="#111"/>
      </svg>
      <span>123 - 456789</span>
    </li>
    <li class="contact__item">
      <svg class="contact__icon" viewBox="0 0 22 22" aria-hidden="true">
        <circle cx="11" cy="11" r="11" fill="var(--gold-soft)"/>
        <circle cx="11" cy="11" r="5" fill="none" stroke="#111" stroke-width="1.2"/>
        <ellipse cx="11" cy="11" rx="2.2" ry="5" fill="none" stroke="#111" stroke-width="1"/>
        <line x1="6" y1="11" x2="16" y2="11" stroke="#111" stroke-width="1"/>
      </svg>
      <span>website.com</span>
    </li>
  </ul>
</section>

</body>
</html>
```